Accounting firm needing business card / letterhead designed
Marcus T. Elbering, CPA
marcus@fernquill.com
www.fernquill.com
482 N Harlow Ave Wrenfield, ND 43719
555-555-0172

```html
<!DOCTYPE html>
<html lang="en">
<head>
<meta charset="utf-8">
<title>Fernquill Business Card</title>
<link rel="stylesheet" href="https://fonts.googleapis.com/css2?family=Source+Sans+3:wght@400;600;700&display=swap">
<style>
  :root {
    --backdrop: #464646;
    --card-light: #f3f3f3;
    --navy: #27235f;
    --green: #8dc63f;
    --ink: #2e2e2e;
  }
  * { margin: 0; padding: 0; box-sizing: border-box; }
  html, body { width: 1200px; height: 900px; overflow: hidden; }
  body {
    background: var(--backdrop);
    font-family: "Source Sans 3", "Myriad Pro", sans-serif;
    position: relative;
  }
  .card {
    position: absolute;
    top: 170px;
    width: 347px;
    height: 561px;
  }
  .card--front { left: 259px; background: var(--card-light); }
  .card--back { left: 631px; background: var(--navy); }

  .brand-name {
    position: absolute;
    left: 0; right: 0;
    text-align: center;
    font-weight: 700;
    font-size: 46px;
    letter-spacing: 1px;
    line-height: 1;
  }
  .card--front .brand-name { top: 128px; color: var(--navy); }
  .card--back .brand-name { top: 254px; color: var(--green); }

  .holder-name {
    position: absolute;
    top: 356px; left: 0; right: 0;
    text-align: center;
    font-weight: 700;
    font-size: 21px;
    color: var(--navy);
    letter-spacing: 0.2px;
  }
  .contact-icons {
    position: absolute;
    top: 405px; left: 0; right: 0;
    display: flex;
    justify-content: center;
    gap: 5px;
  }
  .contact-icons svg { width: 14px; height: 14px; fill: var(--navy); }
  .contact-list {
    position: absolute;
    top: 424px; left: 0; right: 0;
    text-align: center;
    list-style: none;
    font-size: 16px;
    line-height: 20px;
    color: var(--ink);
  }
  .address {
    position: absolute;
    top: 498px; left: 0; right: 0;
    text-align: center;
    font-size: 16px;
    color: var(--ink);
  }
</style>
</head>
<body>
  <section class="card card--front">
    <div class="brand-name">FERNQUILL</div>
    <h1 class="holder-name">MARCUS T. ELBERING, CPA</h1>
    <div class="contact-icons" aria-hidden="true">
      <svg viewBox="0 0 16 16"><path d="M3.6 1.2l2.2 2.6c.3.4.3.9 0 1.3L4.7 6.4c.9 2 2.5 3.6 4.9 4.9l1.3-1.1c.4-.3.9-.3 1.3 0l2.6 2.2c.4.3.4.9.1 1.3l-1.2 1.2C11 16.6 6.4 13.4 4 10.9 1.5 8.5-1.2 4.1 1.1 1.2L2.3.2c.4-.3 1-.2 1.3 1z"/></svg>
      <svg viewBox="0 0 16 16"><path d="M1 3h14v1.2L8 8.8 1 4.2z"/><path d="M1 5.6l7 4.6 7-4.6V13H1z"/></svg>
      <svg viewBox="0 0 16 16"><circle cx="8" cy="8" r="7"/><path d="M4 5c1 0 2 .5 2.2 1.5S5 8 5.5 9 7 10 7 11.5 6.5 13.5 6 14A6 6 0 0 1 2.3 5.5zM10 2.5c.5 1 0 2 1 2.3s2 0 2.5 1A6 6 0 0 1 12.5 12c-.5-1-1.5-1-2-2s.5-1.5 0-2.5-2-.5-2-1.8S9.5 3 10 2.5z" fill="#f3f3f3"/></svg>
    </div>
    <ul class="contact-list">
      <li>555-555-0172</li>
      <li>marcus@fernquill.com</li>
      <li>www.fernquill.com</li>
    </ul>
    <p class="address">482 N Harlow Ave Wrenfield, ND 43719</p>
  </section>

  <section class="card card--back">
    <div class="brand-name">FERNQUILL</div>
  </section>
</body>
</html>
```